Web design for "Vetted Hammer"

We need a web design for a service that we are providing to consumers. We have 4 products or packages that they can choose from. These vary in terms of inclusions and cost. The basic service that we off is that we interview, reference check and verify insurances on tradespeople before a consumer commits with a tradesperson to complete a job.
The web design will need to incorporate two databases. One database for the consumer buying the services and another database for the tradespeople that are being checked.
The cost will be charged to the consumer. The service will be free for tradespeople to join.
The services will be packages based on what the consumer is requiring. There are 4 packages at varying prices. We will need also need a page that has the payment portal.
We will need a rating system (stars or similar), the ability to upload documents, and to send communications.
Updates

Reason: I have only had one designer submit their designs. Would really appreciate a comparison

Target Market(s)

Professionals, time poor people, mainly female target audience

Industry/Entity Type

Business Service

Number of Pages Required

5+ page

Font styles to use
Sans Serif

Colors
abd036
fece3e
b7a5cd
f68d4d
3176b5
cadf82

Requirements
Must have
• 2 x databases, Payment Portal, star rating

```html
<!DOCTYPE html>
<html lang="en">
<head>
<meta charset="utf-8">
<title>Vetted Hammer</title>
<link href="https://fonts.googleapis.com/css2?family=Roboto:wght@300;400;500;700&family=Open+Sans:ital,wght@0,400;0,600;1,400&display=swap" rel="stylesheet">
<style>
:root{
  --blue:#1f6fb2;
  --blue-dark:#123a68;
  --navy:#0f2f57;
  --ink:#222;
  --muted:#9a9a9a;
  --nav:#8a8a8a;
  --line:#d9d9d9;
  --panel:#efefef;
  --footer:#ececec;
  --white:#fff;
  --star:#f5c518;
}
*{box-sizing:border-box;margin:0;padding:0}
html,body{width:1200px;height:2903px;overflow:hidden;background:var(--white)}
body{font-family:"Open Sans",Arial,sans-serif;color:var(--ink);position:relative}
h1,h2,h3,h4{font-family:"Roboto",Arial,sans-serif;font-weight:400}

/* Header */
.site-header{position:absolute;top:0;left:0;width:1200px;height:112px;background:var(--white)}
.brand{position:absolute;left:120px;top:40px;font-family:"Roboto",Arial,sans-serif;font-weight:700;font-size:29px;color:var(--blue-dark);letter-spacing:.3px}
.main-nav{position:absolute;left:452px;top:0;display:flex;height:112px}
.main-nav a{font-family:"Roboto",Arial,sans-serif;font-size:16px;color:var(--nav);text-decoration:none;padding:50px 14px 0;margin-right:10px;position:relative}
.main-nav a.active{color:var(--blue)}
.main-nav a.active::before{content:"";position:absolute;left:2px;right:2px;top:0;height:5px;background:var(--blue)}

/* Hero */
.hero{position:absolute;top:112px;left:0;width:1200px;height:568px}
.hero-photo{position:absolute;inset:0;background:linear-gradient(180deg,#9cc6ea 0%,#d9e9f6 38%,#7e98b0 62%,#2b3d52 80%,#5c89b0 100%)}
.hero-copy{position:absolute;left:118px;top:168px;width:460px;color:var(--white)}
.hero-copy h1{font-size:32px;line-height:38px;text-transform:uppercase;color:#1d3f73;font-weight:400}
.hero-copy p{font-size:15px;line-height:20px;color:#2c3e56;margin-top:12px}
.btn-solid{position:absolute;left:120px;top:320px;width:152px;height:44px;background:var(--blue);color:var(--white);font-family:"Roboto",Arial,sans-serif;font-size:14px;font-weight:500;display:flex;align-items:center;justify-content:center;letter-spacing:.5px}
.hero-dots{position:absolute;top:535px;left:482px;display:flex;gap:10px}
.hero-dots span{width:14px;height:14px;border-radius:50%;background:var(--white);opacity:.75}
.hero-dots span:last-child{opacity:1}

/* About */
.about{position:absolute;top:680px;left:0;width:1200px;height:417px;text-align:center}
.about h2{font-size:34px;margin-top:90px;color:var(--ink)}
.about p{width:800px;margin:22px auto 0;font-size:18px;line-height:25px;color:var(--muted)}
.about p + p{margin-top:14px}
.btn-outline{display:inline-flex;align-items:center;justify-content:center;border:2px solid var(--blue);color:var(--blue);font-family:"Roboto",Arial,sans-serif;font-weight:500;font-size:16px;letter-spacing:.5px;background:var(--white)}
.about .btn-outline{width:172px;height:44px;margin-top:26px}

/* Services */
.services{position:absolute;top:1097px;left:0;width:1200px;height:481px;overflow:hidden}
.services-photo{position:absolute;inset:0;background:linear-gradient(90deg,#0f2f57 0%,#153d6d 38%,#5a6e84 55%,#a6afb6 72%,#3e5f8a 88%,#4c7db0 100%)}
.services-copy{position:absolute;left:122px;top:60px;color:var(--white)}
.services-copy h2{font-size:30px;font-weight:400}
.service{display:flex;align-items:flex-start;margin-top:30px}
.service + .service{margin-top:28px}
.service-icon{width:78px;height:78px;border-radius:50%;background:var(--blue);display:flex;align-items:center;justify-content:center;flex:none}
.service-text{margin-left:15px;margin-top:10px}
.service-text h3{font-size:20px;font-weight:400}
.service-text p{font-size:12px;line-height:19px;color:#c6d3e3;width:300px;margin-top:4px}

/* Packages */
.packages{position:absolute;top:1578px;left:0;width:1200px;height:554px;background:var(--panel);text-align:center}
.packages h2{font-size:30px;margin-top:60px;font-weight:500}
.plan{position:absolute;top:134px;height:308px;background:var(--white);border:1px solid var(--line);border-radius:4px}
.plan h3{font-size:22px;margin-top:24px;color:#333}
.plan ul{list-style:none;width:210px;margin:10px auto 0}
.plan li{font-size:12px;color:#555;padding:7px 0 6px;border-bottom:1px solid var(--line)}
.plan li:last-child{border-bottom:none}
.plan .price{font-family:"Roboto",Arial,sans-serif;font-size:29px;color:var(--blue);margin-top:12px}
.plan .btn-outline{width:126px;height:32px;font-size:12px;margin-top:18px;border-width:2px;border-color:var(--blue-dark);color:var(--blue-dark)}
.plan.featured{background:var(--blue);border-color:var(--blue);color:var(--white);top:125px;height:330px;box-shadow:0 2px 6px rgba(0,0,0,.15)}
.plan.featured h3,.plan.featured li,.plan.featured .price{color:var(--white)}
.plan.featured li{border-color:rgba(255,255,255,.35)}
.plan.featured .btn-outline{background:transparent;border-color:var(--white);color:var(--white);height:34px}

/* Reviews */
.reviews{position:absolute;top:2132px;left:0;width:1200px;height:383px;overflow:hidden;text-align:center}
.reviews-photo{position:absolute;inset:0;background:linear-gradient(180deg,#3e3f42 0%,#2f3236 45%,#4a3f38 80%,#5a4636 100%)}
.reviews h2{position:relative;font-size:32px;color:var(--white);font-weight:300;padding-top:40px}
.review{position:absolute;top:113px;width:297px;height:196px;border:2px solid var(--white);border-radius:4px;color:var(--white);padding:28px 20px 0}
.stars{color:var(--star);font-size:22px;letter-spacing:3px;line-height:22px}
.review p{font-style:italic;font-size:11.5px;line-height:21px;margin-top:10px}
.review cite{display:block;font-style:normal;font-weight:600;font-size:12px;margin-top:8px}
.review-dots{position:absolute;top:346px;left:547px;display:flex;gap:8px}
.review-dots span{width:32px;height:3px;background:#ddd}
.review-dots span.active{background:#3ba3d8}

/* Footer */
.site-footer{position:absolute;top:2515px;left:0;width:1200px;height:388px;background:var(--footer)}
.footer-brand{position:absolute;left:112px;top:78px;width:200px;font-family:"Roboto",Arial,sans-serif;font-weight:700;font-size:27px;line-height:30px;color:var(--blue-dark)}
.footer-col{position:absolute;top:70px}
.footer-col h4{font-size:21px;color:#333}
.footer-col ul{list-style:none;margin-top:14px}
.footer-col li{font-size:14px;color:#666;line-height:31px}
.footer-divider{position:absolute;top:72px;width:1px;height:160px;background:#c9c9c9}
.social{display:flex;gap:8px;margin-top:16px}
.social span{width:40px;height:40px;border-radius:50%;border:2px solid var(--blue)}
.copyright{position:absolute;top:336px;width:1200px;text-align:center;font-size:12px;color:#888}
</style>
</head>
<body>

<header class="site-header">
  <div class="brand">VETTED HAMMER</div>
  <nav class="main-nav">
    <a class="active" href="#">Home</a>
    <a href="#">About Us</a>
    <a href="#">Services</a>
    <a href="#">Packages</a>
    <a href="#">Blogs</a>
    <a href="#">News</a>
    <a href="#">Contact</a>
  </nav>
</header>

<section class="hero">
  <div class="hero-photo" role="img" aria-label="Container ships loaded with cargo at a harbour with cranes under a blue sky"></div>
  <div class="hero-copy">
    <h1>Proin nulla arcu nonu dictum eget ferment</h1>
    <p>Maecenas aliquet velit vel turpis Mauris neque metus malesuada nec ultricies sit</p>
  </div>
  <div class="btn-solid">READ MORE</div>
  <div class="hero-dots"><span></span><span></span><span></span><span></span></div>
</section>

<section class="about">
  <h2>About Vetted Hammer</h2>
  <p>Praesent elementum elit at tellus nec ultricies sit amet porttitor mattis enim In massa libero interdum nec interdum vel blandit sed nulla In ullamcorper est eget tempor</p>
  <p>consectetuer mi a ultricies massa est sed nisl Class aptent taciti sociosqu ad litora torquent per conubiagna hendrerit accumsan Suspendisse</p>
  <div class="btn-outline">LEARN MORE</div>
</section>

<section class="services">
  <div class="services-photo" role="img" aria-label="Two workers in hard hats and safety vests inspecting a port loading area"></div>
  <div class="services-copy">
    <h2>Our Services</h2>
    <div class="service">
      <div class="service-icon">
        <svg width="44" height="44" viewBox="0 0 44 44" fill="none" stroke="#fff" stroke-width="2.4">
          <circle cx="12" cy="14" r="4"/><circle cx="32" cy="14" r="4"/>
          <path d="M5 30v-6c0-3 3-5 7-5s7 2 7 5v6M25 30v-6c0-3 3-5 7-5s7 2 7 5v6M6 34h32"/>
        </svg>
      </div>
      <div class="service-text"><h3>Interview</h3><p>sociosqu ad litora torquent per conubia nostra per inceptos hymenaeos Proin nulla arcu</p></div>
    </div>
    <div class="service">
      <div class="service-icon">
        <svg width="42" height="42" viewBox="0 0 42 42" fill="none" stroke="#fff" stroke-width="2.4">
          <path d="M21 5l13 5v10c0 9-6 14-13 17C14 34 8 29 8 20V10z"/><path d="M15 21l4 4 8-8"/>
        </svg>
      </div>
      <div class="service-text"><h3>Verify insurances</h3><p>sociosqu ad litora torquent per conubia nostra per inceptos hymenaeos Proin nulla arcu</p></div>
    </div>
    <div class="service">
      <div class="service-icon">
        <svg width="42" height="42" viewBox="0 0 42 42" fill="none" stroke="#fff" stroke-width="2.2">
          <circle cx="21" cy="21" r="14"/><ellipse cx="21" cy="21" rx="6" ry="14"/><path d="M7 21h28M9 14h24M9 28h24"/>
        </svg>
      </div>
      <div class="service-text"><h3>Reference Check</h3><p>sociosqu ad litora torquent per conubia nostra per inceptos hymenaeos Proin nulla arcu</p></div>
    </div>
  </div>
</section>

<section class="packages">
  <h2>Our Packages</h2>
  <div class="plan" style="left:120px;width:240px">
    <h3>BASIC</h3>
    <ul><li>Sociosqu ad litora torquent</li><li>Per conubia nostra</li><li>Aer inceptos hymenaeos</li><li>Proin nulla arcu</li><li>Nonummy luctus dictum</li></ul>
    <div class="price">$25.99</div>
    <div class="btn-outline">GET STARTED</div>
  </div>
  <div class="plan" style="left:372px;width:240px">
    <h3>BUSINESS</h3>
    <ul><li>Sociosqu ad litora torquent</li><li>Per conubia nostra</li><li>Aer inceptos hymenaeos</li><li>Proin nulla arcu</li><li>Nonummy luctus dictum</li></ul>
    <div class="price">$55.99</div>
    <div class="btn-outline">GET STARTED</div>
  </div>
  <div class="plan featured" style="left:607px;width:254px">
    <h3>PRO</h3>
    <ul><li>Sociosqu ad litora torquent</li><li>Per conubia nostra</li><li>Aer inceptos hymenaeos</li><li>Proin nulla arcu</li><li>Nonummy luctus dictum</li></ul>
    <div class="price">$75.99</div>
    <div class="btn-outline">GET STARTED</div>
  </div>
  <div class="plan" style="left:862px;width:234px">
    <h3>ADVANCED</h3>
    <ul><li>Sociosqu ad litora torquent</li><li>Per conubia nostra</li><li>Aer inceptos hymenaeos</li><li>Proin nulla arcu</li><li>Nonummy luctus dictum</li></ul>
    <div class="price">$95.99</div>
    <div class="btn-outline">GET STARTED</div>
  </div>
</section>

<section class="reviews">
  <div class="reviews-photo" role="img" aria-label="Dimmed view of a busy container port at dusk"></div>
  <h2>Latest Review</h2>
  <div class="review" style="left:150px">
    <div class="stars">★★★★</div>
    <p>sociosqu ad litora torquent per conubia nostra per inceptos hymenaeos Proin nulla arcu nonummy luctus dictum eget fermentum et lorem Nunc porta convallis pede</p>
    <cite>By Author Name</cite>
  </div>
  <div class="review" style="left:461px">
    <div class="stars">★★★★</div>
    <p>sociosqu ad litora torquent per conubia nostra per inceptos hymenaeos Proin nulla arcu nonummy luctus dictum eget fermentum et lorem Nunc porta convallis pede</p>
    <cite>By Author Name</cite>
  </div>
  <div class="review" style="left:772px">
    <div class="stars">★★★★</div>
    <p>sociosqu ad litora torquent per conubia nostra per inceptos hymenaeos Proin nulla arcu nonummy luctus dictum eget fermentum et lorem Nunc porta convallis pede</p>
    <cite>By Author Name</cite>
  </div>
  <div class="review-dots"><span></span><span></span><span class="active"></span></div>
</section>

<footer class="site-footer">
  <div class="footer-brand">VETTED HAMMER</div>
  <div class="footer-col" style="left:328px">
    <h4>Company</h4>
    <ul><li>Home</li><li>About Us</li><li>Products</li><li>Why Us</li></ul>
  </div>
  <div class="footer-divider" style="left:460px"></div>
  <div class="footer-col" style="left:510px">
    <h4>Support</h4>
    <ul><li>FAQ</li><li>Support</li><li>Term of Use</li><li>Contact Us</li></ul>
  </div>
  <div class="footer-divider" style="left:641px"></div>
  <div class="footer-col" style="left:694px">
    <h4>Resources</h4>
    <ul><li>Our Video</li><li>Blogs</li><li>News</li></ul>
  </div>
  <div class="footer-divider" style="left:822px"></div>
  <div class="footer-col" style="left:861px">
    <h4>Say in Touch</h4>
    <div class="social"><span></span><span></span><span></span><span></span></div>
  </div>
  <div class="copyright">© 2017 Company Name &nbsp;All right reserved &nbsp;Term of Use</div>
</footer>

</body>
</html>
```